KESTRALINE, LLC needs a hybrid app to evaluate and develop athletes

KESTRALINE, LLC needs initial hybrid mobile app and website holding page. KESTRALINE, LLC allows athletes to develop their skills (soccer is initial sport) for free. Receive daily/weekly reminders. Access training videos. Earn points to "upgrade" their soccer profile in "app soccer store". See their points/rankings compared to all app users. Progress streak. This free app (for athletes) will communicate to paid app (coaches) in the future. We would like to see designs use the color blue. The design will communicate health and wellness.
Coded - Design and coding required
5+ page

```html
<!DOCTYPE html>
<html lang="en">
<head>
<meta charset="utf-8">
<title>KESTRALINE, LLC — App Screens</title>
<link href="https://fonts.googleapis.com/css2?family=Ultra&family=Roboto+Slab:wght@400;500&family=Lato:wght@400;700&display=swap" rel="stylesheet">
<style>
  :root{
    --board:#8a8a8a;
    --navy:#1b3f91;
    --hero-top:#0d3a9c;
    --hero-bottom:#0b2a6e;
    --pale:#c5d6e8;
    --btn:#7a9fcf;
    --row-blue:#2a5ca5;
    --white:#ffffff;
    --ink:#222831;
    --grey-icon:#454a52;
    --green:#2bb52b;
    --card-line:#c9d3e6;
  }
  *{margin:0;padding:0;box-sizing:border-box}
  html,body{width:1200px;height:2183px;overflow:hidden;background:var(--board)}
  .board{position:absolute;left:0;top:0;width:1094px;height:1990px;transform:scale(1.09689);transform-origin:0 0;font-family:'Lato',sans-serif}
  .screen{position:absolute;width:450px;overflow:hidden}
  .screen.auth{height:768px;top:72px}
  .screen.app{height:1032px;top:891px;background:var(--white)}
  .col-left{left:73px}.col-right{left:585px}
  .hero-bg{position:absolute;inset:0;background:linear-gradient(180deg,var(--hero-top) 0%,#12439f 45%,var(--hero-bottom) 100%)}
  .abs{position:absolute}
  .rule{position:absolute;height:3px;background:var(--white)}
  .rule.long{left:91px;width:269px}
  .rule.short{left:158px;width:135px}
  .brand{position:absolute;left:0;width:450px;text-align:center;font-family:'Ultra',serif;color:var(--white);font-size:34px;line-height:40px;letter-spacing:1px}
  .heading{position:absolute;left:0;width:450px;text-align:center;font-family:'Ultra',serif;color:var(--white);font-size:21px;letter-spacing:1px;line-height:26px}
  .field{position:absolute;left:40px;width:371px;height:54px;border-radius:27px;background:var(--white);color:var(--ink);font-size:18px;line-height:54px;padding-left:26px}
  .field.with-icon{padding-left:70px}
  .field svg.icon{position:absolute;left:32px;top:19px}
  .field svg.select{position:absolute;right:22px;top:19px}
  .btn{position:absolute;left:40px;width:371px;height:54px;border-radius:27px;background:var(--btn);color:var(--white);font-family:'Ultra',serif;font-size:21px;letter-spacing:1px;text-align:center;line-height:54px}
  .links{position:absolute;left:0;width:450px;text-align:center;color:var(--white);font-size:14px;letter-spacing:.3px}
  .links u{text-underline-offset:2px}
  .legal{position:absolute;left:0;width:450px;text-align:center;color:var(--white);font-size:14px;line-height:26px}
  .scale-note{position:absolute;font-size:14px;color:var(--white)}
  .app .scale-note{color:var(--navy)}
  .app-header{position:absolute;left:0;top:0;width:450px;height:147px;overflow:hidden}
  .title-band{position:absolute;left:0;top:147px;width:450px;height:111px;background:var(--pale)}
  .page-title{position:absolute;left:0;top:187px;width:450px;text-align:center;font-family:'Ultra',serif;color:var(--navy);font-size:26px;letter-spacing:.5px;line-height:32px}
  .badge-art{position:absolute;left:20px;top:175px;width:62px;height:58px;border-radius:50%;background:radial-gradient(circle at 60% 60%,#ffffff 0 30%,#f7a81b 31% 55%,#e2401b 56% 100%)}
  .white-band{position:absolute;left:0;top:258px;width:450px;height:170px;background:var(--white)}
  .pale-panel{position:absolute;left:0;top:428px;width:450px;height:525px;background:var(--pale)}
  .team-card{position:absolute;left:18px;top:287px;width:107px;height:111px;border:1px solid #b9c2cf;border-bottom:3px solid var(--green);border-radius:10px;background:var(--white)}
  .team-art{position:absolute;border-radius:50%}
  .team-label{position:absolute;font-family:'Ultra',serif;color:var(--navy);font-size:14px;line-height:18px;text-align:center}
  .count{position:absolute;left:0;top:460px;width:450px;text-align:center;font-family:'Roboto Slab',serif;font-weight:500;color:var(--navy);font-size:22px;letter-spacing:1px}
  .rank-row{position:absolute;left:40px;width:371px;height:54px;border-radius:27px;background:var(--white);overflow:hidden}
  .rank-row.current{box-shadow:0 0 0 3px var(--green)}
  .rank-name{position:absolute;left:0;top:0;width:95px;height:54px;background:var(--row-blue);color:var(--white);font-family:'Ultra',serif;font-size:18px;line-height:54px;text-align:center}
  .rank-id{position:absolute;left:117px;top:0;line-height:54px;font-family:'Roboto Slab',serif;font-size:17px;color:var(--ink);letter-spacing:.5px}
  .tab-bar{position:absolute;left:0;top:953px;width:450px;height:79px;background:var(--white)}
  .tab-bar svg{position:absolute}
  .profile-card{position:absolute;left:17px;top:287px;width:416px;height:170px;border:1px solid var(--card-line);border-radius:12px;background:var(--white)}
  .avatar{position:absolute;left:13px;top:10px;width:86px;height:86px;border-radius:50%;background:linear-gradient(160deg,#d9dde3,#9aa6b5)}
  .athlete-id{position:absolute;left:120px;top:15px;font-family:'Roboto Slab',serif;font-size:16px;color:var(--navy)}
  .athlete-name{position:absolute;left:120px;top:38px;font-size:23px;color:var(--ink)}
  .athlete-stats{position:absolute;left:120px;top:76px;font-size:15px;color:var(--navy);font-weight:700}
  .stat-line{position:absolute;left:120px;width:262px;font-size:14.5px;font-weight:700;color:var(--ink)}
  .stat-line span{position:absolute;right:0}
  .score{position:absolute;left:364px;top:9px;width:34px;height:34px;border-radius:50%;background:var(--navy);color:var(--white);font-size:15px;font-weight:700;text-align:center;line-height:34px}
  .hero-art{position:absolute;left:0;top:480px;width:450px;height:473px;background:radial-gradient(ellipse at 50% 55%,#f6f8fc 0%,#e4ebf5 55%,#d5e0ee 100%)}
</style>
</head>
<body>
<div class="board">

  <!-- Athlete login -->
  <section class="screen auth col-left">
    <div class="hero-bg" role="img" aria-label="Photo of soccer players in action, tinted deep blue"></div>
    <div class="rule long" style="top:96px"></div>
    <h1 class="brand" style="top:110px">KESTRALINE, LLC</h1>
    <div class="rule short" style="top:163px"></div>
    <h2 class="heading" style="top:250px">ATHLETE LOGIN</h2>
    <div class="field with-icon" style="top:300px">
      <svg class="icon" width="16" height="16" viewBox="0 0 16 16"><circle cx="8" cy="5" r="4" fill="#8a8f96"/><path d="M1 16c0-5 3-7 7-7s7 2 7 7z" fill="#8a8f96"/></svg>
      Username
    </div>
    <div class="field with-icon" style="top:370px">
      <svg class="icon" width="16" height="16" viewBox="0 0 16 16"><circle cx="5" cy="5" r="3.5" fill="none" stroke="#8a8f96" stroke-width="2"/><path d="M7.5 7.5 15 15M11 11l2-2M13 13l2-2" stroke="#8a8f96" stroke-width="2"/></svg>
      Password
    </div>
    <div class="btn" style="top:440px">LOGIN</div>
    <p class="links" style="top:532px">CREATE ACCOUNT &nbsp;|&nbsp; <u>FORGOT PASSWORD</u></p>
    <p class="legal" style="top:681px">Copyright © 2020 Company Name<br>All Right Reserved</p>
    <span class="scale-note" style="left:414px;top:736px">x10</span>
  </section>

  <!-- Create account -->
  <section class="screen auth col-right">
    <div class="hero-bg" role="img" aria-label="Photo of soccer players in action, tinted deep blue"></div>
    <div class="rule long" style="top:64px"></div>
    <h1 class="brand" style="top:78px">KESTRALINE, LLC</h1>
    <div class="rule short" style="top:131px"></div>
    <h2 class="heading" style="top:209px">CREATE ACCOUNT</h2>
    <div class="field" style="top:253px">Name</div>
    <div class="field" style="top:323px;width:180px">Age
      <svg class="select" width="10" height="16" viewBox="0 0 10 16"><path d="M5 0 10 6H0zM5 16 0 10h10z" fill="#222831"/></svg></div>
    <div class="field" style="top:323px;left:230px;width:181px;padding-left:22px">Gender
      <svg class="select" width="10" height="16" viewBox="0 0 10 16"><path d="M5 0 10 6H0zM5 16 0 10h10z" fill="#222831"/></svg></div>
    <div class="field" style="top:393px">Country
      <svg class="select" width="10" height="16" viewBox="0 0 10 16"><path d="M5 0 10 6H0zM5 16 0 10h10z" fill="#222831"/></svg></div>
    <div class="field" style="top:463px">State/ZIP or Region</div>
    <div class="btn" style="top:533px">CREATE ACCOUNT</div>
    <p class="legal" style="top:681px">Copyright © 2020 Company Name<br>All Right Reserved</p>
    <span class="scale-note" style="left:414px;top:736px">x10</span>
  </section>

  <!-- Leaderboard -->
  <section class="screen app col-left">
    <div class="app-header">
      <div class="hero-bg" role="img" aria-label="Photo of soccer players in action, tinted deep blue"></div>
      <div class="rule long" style="top:39px"></div>
      <h1 class="brand" style="top:53px">KESTRALINE, LLC</h1>
      <div class="rule short" style="top:106px"></div>
    </div>
    <div class="title-band"></div>
    <div class="badge-art" role="img" aria-label="Flaming soccer ball illustration"></div>
    <h2 class="page-title" style="left:0">LEADERBOARD</h2>
    <div class="white-band"></div>
    <div class="team-card">
      <div class="team-art" role="img" aria-label="Illustration of three teammates with a ball" style="left:24px;top:10px;width:58px;height:50px;border-radius:12px;background:linear-gradient(180deg,#f2c39a,#3d6fc0)"></div>
      <div class="team-label" style="left:0;top:75px;width:105px">MY TEAM</div>
    </div>
    <div class="team-art" role="img" aria-label="Illustration of a team in front of a globe" style="left:335px;top:288px;width:57px;height:57px;background:linear-gradient(180deg,#6aa8e0,#2f65b0)"></div>
    <div class="team-label" style="left:293px;top:361px;width:140px">KESTRALINE<br>TEAM</div>
    <div class="pale-panel"></div>
    <div class="count">4 / 18</div>
    <div class="rank-row" style="top:504px"><span class="rank-name">Yaa</span><span class="rank-id">#12345</span></div>
    <div class="rank-row" style="top:572px"><span class="rank-name">Yaa</span><span class="rank-id">#6789</span></div>
    <div class="rank-row" style="top:641px"><span class="rank-name">Yaa</span><span class="rank-id">#2468</span></div>
    <div class="rank-row current" style="top:709px"><span class="rank-name">Yaa</span><span class="rank-id">#1357</span></div>
    <div class="rank-row" style="top:779px"><span class="rank-name">Yaa</span><span class="rank-id">#1256</span></div>
    <div class="rank-row" style="top:847px"><span class="rank-name">Yaa</span><span class="rank-id">#3478</span></div>
    <nav class="tab-bar">
      <svg style="left:33px;top:16px" width="44" height="44" viewBox="0 0 44 44"><circle cx="28" cy="14" r="10" fill="none" stroke="#454a52" stroke-width="2"/><path d="M28 9l4 3-1.5 5h-5L24 12z" fill="#454a52"/><path d="M20 20 6 38M23 24 10 41M17 16 3 32" stroke="#454a52" stroke-width="2" fill="none"/></svg>
      <svg style="left:134px;top:17px" width="46" height="46" viewBox="0 0 46 46"><circle cx="23" cy="23" r="22" fill="#454a52"/><circle cx="23" cy="18" r="8" fill="#fff"/><path d="M9 37c3-8 8-10 14-10s11 2 14 10a20 20 0 0 1-28 0z" fill="#fff"/></svg>
      <svg style="left:239px;top:16px" width="40" height="46" viewBox="0 0 40 46"><path d="M20 1 38 8v13c0 12-8 20-18 24C10 41 2 33 2 21V8z" fill="#454a52"/><path d="M20 7 32 12v10c0 8-5 14-12 17z" fill="#fff"/></svg>
      <svg style="left:354px;top:22px" width="72" height="34" viewBox="0 0 72 34"><path d="M2 10c8-8 18-10 26-6l10 6c8 2 20 4 28 8 4 2 4 8-2 8H6c-4 0-6-3-6-6z" fill="#454a52"/><path d="M8 27h4v5H8zM22 27h4v5h-4zM40 27h4v5h-4zM56 27h4v5h-4z" fill="#454a52"/></svg>
      <span class="scale-note" style="left:420px;top:58px">x10</span>
    </nav>
  </section>

  <!-- Profile -->
  <section class="screen app col-right">
    <div class="app-header">
      <div class="hero-bg" role="img" aria-label="Photo of soccer players in action, tinted deep blue"></div>
      <div class="rule long" style="top:39px"></div>
      <h1 class="brand" style="top:53px">KESTRALINE, LLC</h1>
      <div class="rule short" style="top:106px"></div>
    </div>
    <div class="title-band"></div>
    <div class="badge-art" role="img" aria-label="Flaming soccer ball illustration"></div>
    <h2 class="page-title">PROFILE</h2>
    <div class="white-band" style="height:222px"></div>
    <article class="profile-card">
      <div class="avatar" role="img" aria-label="Athlete portrait photo"></div>
      <div class="athlete-id">#AZ12345</div>
      <div class="athlete-name">Marco Velden</div>
      <div class="athlete-stats">18 / M / 6’2 / 200</div>
      <div class="stat-line" style="top:107px">Primary Position:<span>7</span></div>
      <div class="stat-line" style="top:136px">Secondary Position:<span>5</span></div>
      <div class="score">82</div>
    </article>
    <div class="hero-art" role="img" aria-label="Illustration of a young soccer player in a red number 1 jersey with his foot on a ball"></div>
    <nav class="tab-bar">
      <svg style="left:33px;top:16px" width="44" height="44" viewBox="0 0 44 44"><circle cx="28" cy="14" r="10" fill="none" stroke="#454a52" stroke-width="2"/><path d="M28 9l4 3-1.5 5h-5L24 12z" fill="#454a52"/><path d="M20 20 6 38M23 24 10 41M17 16 3 32" stroke="#454a52" stroke-width="2" fill="none"/></svg>
      <svg style="left:134px;top:17px" width="46" height="46" viewBox="0 0 46 46"><circle cx="23" cy="23" r="22" fill="#454a52"/><circle cx="23" cy="18" r="8" fill="#fff"/><path d="M9 37c3-8 8-10 14-10s11 2 14 10a20 20 0 0 1-28 0z" fill="#fff"/></svg>
      <svg style="left:239px;top:16px" width="40" height="46" viewBox="0 0 40 46"><path d="M20 1 38 8v13c0 12-8 20-18 24C10 41 2 33 2 21V8z" fill="#454a52"/><path d="M20 7 32 12v10c0 8-5 14-12 17z" fill="#fff"/></svg>
      <svg style="left:354px;top:22px" width="72" height="34" viewBox="0 0 72 34"><path d="M2 10c8-8 18-10 26-6l10 6c8 2 20 4 28 8 4 2 4 8-2 8H6c-4 0-6-3-6-6z" fill="#454a52"/><path d="M8 27h4v5H8zM22 27h4v5h-4zM40 27h4v5h-4zM56 27h4v5h-4z" fill="#454a52"/></svg>
      <span class="scale-note" style="left:420px;top:58px">x10</span>
    </nav>
  </section>

</div>
</body>
</html>
```